Business Card Re-design

We are looking for a fresh bold look for general office business cards. We are a staffing agency that staffs industrial, coal mining, and clerical jobs.
Tag Line: We pair strong teams with steady work across the region.
Harlow Falls Office: 2473 W. Tallow Creek Rd, Harlow Falls, IN - 47308
p. 555.203.6180 f. 555.203.6195
Cedar Bend Office: 264 S. Birch Ln, Cedar Bend, IN - 47152
p. 555.319.2047 f. 555.203.6195
Absentee/Emergency 24hr Hotline 555.203.6172 opt.1
www.bluelanternworkforce.example

```html
<!DOCTYPE html>
<html lang="en">
<head>
<meta charset="UTF-8">
<title>Blue Lantern Workforce – Business Card</title>
<link href="https://fonts.googleapis.com/css2?family=Raleway:wght@500;600;700&display=swap" rel="stylesheet">
<style>
  :root {
    --board: #bcbdbf;
    --paper: #ffffff;
    --navy: #173d69;
    --accent-navy: #2e4a7d;
    --accent-light: #7dbde2;
    --leaf: #6ab645;
  }
  * { margin: 0; padding: 0; box-sizing: border-box; }
  html, body { width: 1200px; height: 1200px; overflow: hidden; }
  body {
    background: var(--board);
    font-family: "Raleway", sans-serif;
    color: var(--navy);
    position: relative;
  }
  .card {
    position: absolute;
    width: 840px;
    height: 480px;
    background: var(--paper);
    overflow: hidden;
  }
  .card--front { left: 177px; top: 38px; }
  .card--back { left: 187px; top: 627px; }

  .corner-accent {
    position: absolute;
    right: -260px;
    bottom: -230px;
    width: 520px;
    height: 460px;
    border-radius: 50%;
    background: linear-gradient(135deg, var(--accent-navy) 20%, var(--accent-light) 55%, var(--leaf) 85%);
  }

  .brand {
    position: absolute;
    display: flex;
    align-items: center;
    gap: 14px;
  }
  .brand__mark {
    width: 26px; height: 26px;
    background: var(--navy);
    flex: none;
  }
  .brand__name {
    font-weight: 700;
    color: var(--navy);
    text-transform: uppercase;
    line-height: 1.02;
    letter-spacing: 0.02em;
  }
  .card--front .brand { left: 27px; top: 40px; }
  .card--front .brand__name { font-size: 38px; }
  .card--back .brand { left: 214px; top: 150px; }
  .card--back .brand__name { font-size: 52px; }

  .tagline {
    position: absolute;
    left: 561px; top: 22px;
    font-size: 18.5px;
    font-weight: 500;
    line-height: 24px;
    text-transform: uppercase;
  }
  .contact {
    position: absolute;
    left: 35px;
    font-size: 21px;
    font-weight: 600;
    line-height: 28px;
  }
  .contact--north { top: 212px; }
  .contact--south { left: 32px; top: 292px; }
  .contact--hotline { top: 396px; }
  .web {
    position: absolute;
    left: 35px; top: 451px;
    font-size: 15.5px;
    font-weight: 600;
  }
  .web--spaced {
    left: 0; right: 0; top: 33px;
    text-align: center;
    font-size: 14.5px;
    font-weight: 500;
    letter-spacing: 0.62em;
    text-transform: uppercase;
    padding-left: 40px;
  }
</style>
</head>
<body>

<section class="card card--front">
  <div class="corner-accent" role="img" aria-label="Decorative corner artwork in navy, sky blue and green"></div>

  <div class="brand">
    <span class="brand__mark"></span>
    <span class="brand__name">Blue<br>Lantern<br>Workforce</span>
  </div>

  <p class="tagline">We pair strong teams<br>with steady work<br>across the region</p>

  <p class="contact contact--north">Harlow Falls Office: 2473 W. Tallow Creek Rd, Harlow Falls, IN - 47308<br>p. 555.203.6180 f. 555.203.6195</p>
  <p class="contact contact--south">Cedar Bend Office: 264 S. Birch Ln, Cedar Bend, IN - 47152<br>p. 555.319.2047 f. 555.203.6195</p>
  <p class="contact contact--hotline">Absentee/Emergency 24hr Hotline 555.203.6172 opt.1</p>

  <p class="web">www.bluelanternworkforce.example</p>
</section>

<section class="card card--back">
  <div class="corner-accent" role="img" aria-label="Decorative corner artwork in navy, sky blue and green"></div>

  <p class="web web--spaced">www.bluelanternworkforce.example</p>

  <div class="brand">
    <span class="brand__mark"></span>
    <span class="brand__name">Blue<br>Lantern<br>Workforce</span>
  </div>
</section>

</body>
</html>
```